Vision / Mission Poster Required

We are looking to display our company Vision / Mission / Values on a poster. This will be displayed in the head office and other site offices.

The document needs to look professional however still be fun, eye catching and easy to read. It will be predominantly displayed in A3 format.

The design needs to use our company Logo which is attached along with the Text to display on the poster. I have put some additional text on the doc that you can include if it suits the layout but is not essential.

Target Market(s)

Staff, Corporate Visitors

Industry/Entity Type

Electric Company

Font styles to use
Sans Serif

Colors

Designer to choose colors to be used in the design.

Requirements
Must have
• Incorporate Logo
• Professional Look
• Attention grabbing
• Easy to Read
Should not have
• Lightning Bolts
• Pictures of random people/Things

```html
<!DOCTYPE html>
<html lang="en">
<head>
<meta charset="utf-8">
<title>Lumen Electrical – Mission, Vision &amp; Values</title>
<link href="https://fonts.googleapis.com/css2?family=Oswald:wght@500;700&family=Lato:wght@400;700;900&display=swap" rel="stylesheet">
<style>
  :root {
    --navy: #0d2e5c;
    --blue: #0f4fa0;
    --orange: #f26b21;
    --ink: #2b2b2b;
    --panel: #ededed;
    --dark: #2a2a2a;
    --stage: #ececec;
  }
  * { box-sizing: border-box; margin: 0; padding: 0; }
  html, body { width: 1200px; height: 1200px; overflow: hidden; background: var(--stage); }
  body { position: relative; font-family: "Lato", sans-serif; color: var(--ink); }

  .poster {
    position: absolute; left: 191px; top: 25px;
    width: 937px; height: 1317px;
    transform: scale(0.873); transform-origin: 0 0;
    background: #fff; overflow: hidden;
  }
  .abs { position: absolute; }

  .hero {
    left: 0; top: 0; width: 937px; height: 604px;
    background:
      radial-gradient(ellipse at 30% 25%, rgba(240,200,30,.75), transparent 55%),
      radial-gradient(ellipse at 80% 70%, rgba(230,170,90,.6), transparent 45%),
      linear-gradient(160deg, #3a2c12 0%, #5a4414 40%, #2a2418 70%, #1b1d24 100%);
  }
  .headline {
    font-family: "Oswald", sans-serif; font-weight: 700; color: #fff;
    font-size: 56px; line-height: 1; letter-spacing: .5px;
    padding-left: 27px; display: flex; align-items: center;
  }
  .headline--navy { left: 0; top: 446px; width: 487px; height: 60px; background: var(--navy); }
  .headline--orange { left: 0; top: 506px; width: 535px; height: 62px; background: var(--orange); }

  .rule-navy { left: 0; top: 604px; width: 937px; height: 8px; background: var(--navy); }
  .rule-blue { left: 0; top: 616px; width: 937px; height: 6px; background: var(--blue); }

  .tag {
    height: 34px; padding-left: 8px; display: flex; align-items: center;
    font-family: "Oswald", sans-serif; font-weight: 700; font-size: 21px; color: #fff;
    clip-path: polygon(0 0, 100% 0, 86% 100%, 0 100%);
  }
  .tag--orange { background: var(--orange); }
  .tag--navy { background: var(--navy); }

  .list-item { display: flex; flex-direction: column; }
  .item-head {
    display: flex; align-items: center; gap: 5px;
    font-weight: 700; font-size: 13px; color: #1a1a1a; height: 18px;
  }
  .item-head svg { width: 14px; height: 14px; flex: none; }
  .item-body { font-size: 13px; line-height: 16px; margin-top: 6px; }

  .mission { left: 30px; top: 684px; width: 380px; }
  .mission .list-item { margin-bottom: 9px; }

  .orange-rule { left: 0; top: 918px; width: 468px; height: 6px; background: var(--orange); }
  .statement {
    left: 0; top: 936px; width: 468px; height: 194px;
    background: linear-gradient(135deg, var(--navy) 0%, var(--blue) 55%, var(--navy) 100%);
    color: #fff; font-size: 13px; line-height: 15.8px; padding: 17px 18px 0 29px;
  }
  .statement p + p { margin-top: 15px; }

  .side-panel {
    left: 494px; top: 622px; width: 443px; height: 498px;
    background: linear-gradient(90deg, #e4e4e4 0%, #f7f7f7 60%, #efefef 100%);
  }
  .vision-text { left: 524px; top: 681px; font-size: 13px; }
  .values { left: 515px; top: 765px; width: 390px; }
  .values .list-item { margin-bottom: 8px; }
  .values .item-body { text-align: justify; }

  .brand { left: 26px; top: 1170px; width: 450px; display: flex; align-items: center; gap: 22px; }
  .brand-dot { width: 92px; height: 92px; border-radius: 50%; background: var(--orange); flex: none; }
  .brand-name {
    font-family: "Lato", sans-serif; font-weight: 900; color: var(--navy);
    font-size: 44px; line-height: 44px; letter-spacing: 1px;
  }

  .office-label { left: 520px; top: 1132px; font-family: "Oswald", sans-serif; font-weight: 500; font-size: 15px; color: #222; }
  .map {
    left: 518px; top: 1155px; width: 183px; height: 114px;
    border: 2px solid var(--orange); border-radius: 6px;
    background: linear-gradient(110deg, #ebe6dc 0%, #e8e3d8 55%, #a9c8f0 70%, #9cc0ee 85%, #e6e2d8 100%);
  }

  .contact { left: 752px; top: 1156px; width: 180px; }
  .contact-row { display: flex; align-items: flex-start; gap: 9px; font-size: 13px; line-height: 15.5px; }
  .contact-row svg { width: 13px; height: 13px; flex: none; margin-top: 2px; }
  .contact-row--phone { font-size: 20px; color: var(--orange); font-weight: 400; line-height: 22px; margin-bottom: 9px; }
  .contact-row--phone svg { margin-top: 5px; }
  .contact-row + .contact-row { margin-top: 6px; }

  .foot-bar { left: 0; top: 1288px; width: 937px; height: 29px; background: linear-gradient(90deg, #1e1e1e, #4a4a4a 45%, #1e1e1e); }
</style>
</head>
<body>
<div class="poster">

  <div class="abs hero" role="img" aria-label="Photograph of a lit café interior with hexagonal yellow ceiling lights and a shopfront"></div>
  <div class="abs headline headline--navy">DYNAMIC RESULTS</div>
  <div class="abs headline headline--orange">PROVEN REPUTATION</div>
  <div class="abs rule-navy"></div>
  <div class="abs rule-blue"></div>

  <div class="abs tag tag--orange" style="left:20px; top:643px; width:124px;">Mission</div>
  <div class="abs mission">
    <div class="list-item">
      <div class="item-head"><svg viewBox="0 0 14 14"><circle cx="7" cy="7" r="6" fill="none" stroke="#0d2e5c" stroke-width="1.4"/><path d="M5.5 4 L8.5 7 L5.5 10" fill="none" stroke="#0d2e5c" stroke-width="1.6"/></svg>Deliver Growth and Value</div>
      <div class="item-body">By: - Maintaining a market presence - Leveraging our technical resources – Networking and developing stakeholder relationships</div>
    </div>
    <div class="list-item">
      <div class="item-head"><svg viewBox="0 0 14 14"><circle cx="7" cy="7" r="6" fill="none" stroke="#0d2e5c" stroke-width="1.4"/><path d="M5.5 4 L8.5 7 L5.5 10" fill="none" stroke="#0d2e5c" stroke-width="1.6"/></svg>Remain Profitable</div>
      <div class="item-body">By: - Increasing revenue – Optimizing capacity utilization<br>– Maintaining expenses</div>
    </div>
    <div class="list-item">
      <div class="item-head"><svg viewBox="0 0 14 14"><circle cx="7" cy="7" r="6" fill="none" stroke="#0d2e5c" stroke-width="1.4"/><path d="M5.5 4 L8.5 7 L5.5 10" fill="none" stroke="#0d2e5c" stroke-width="1.6"/></svg>Be Sustainable</div>
      <div class="item-body">By: - Improving internal efficiency – Diversifying our income sources – Implementing Social &amp; Environmental improvement initiatives</div>
    </div>
  </div>

  <div class="abs orange-rule"></div>
  <div class="abs statement">
    <p>Serving utilities, builders, large private and commercial clients Lumen Electrical is committed to leading the industry in safety, training and customer satisfaction. We will meet and exceed expectations through our full-spectrum of electrical design, build and maintenance services, state-of-the-art assets and financial strength.</p>
    <p>We will continue to embrace new technologies as they emerge and will pursue new and emerging markets. We will maintain our business beliefs and pursue unique and challenging projects to help build a culture that nurtures innovative thinking and strategic planning.</p>
  </div>

  <div class="abs side-panel"></div>
  <div class="abs tag tag--orange" style="left:513px; top:642px; width:123px;">Vision</div>
  <div class="abs vision-text">To be Perth’s premier provider of electrical service solutions</div>
  <div class="abs tag tag--navy" style="left:513px; top:723px; width:123px;">Values</div>

  <div class="abs values">
    <div class="list-item">
      <div class="item-head"><svg viewBox="0 0 14 14"><circle cx="7" cy="7" r="6" fill="none" stroke="#f26b21" stroke-width="1.4"/><path d="M5.5 4 L8.5 7 L5.5 10" fill="none" stroke="#f26b21" stroke-width="1.6"/></svg>Honesty &amp; Integrity</div>
      <div class="item-body">Customers, contractors and suppliers will be able to count on Lumen personnel to deal straightforwardly and adhere to the strictest moral and ethical codes of conduct.</div>
    </div>
    <div class="list-item">
      <div class="item-head"><svg viewBox="0 0 14 14"><circle cx="7" cy="7" r="6" fill="none" stroke="#f26b21" stroke-width="1.4"/><path d="M5.5 4 L8.5 7 L5.5 10" fill="none" stroke="#f26b21" stroke-width="1.6"/></svg>Safety &amp; Responsibility</div>
      <div class="item-body">Lumen is committed to constantly improving safety practices at project job sites and within the electrical service industry as a whole.</div>
    </div>
    <div class="list-item">
      <div class="item-head"><svg viewBox="0 0 14 14"><circle cx="7" cy="7" r="6" fill="none" stroke="#f26b21" stroke-width="1.4"/><path d="M5.5 4 L8.5 7 L5.5 10" fill="none" stroke="#f26b21" stroke-width="1.6"/></svg>Commitment to Quality</div>
      <div class="item-body">Customers and stakeholders will be able to count on Lumen’s workmanship being among the best in the industry.</div>
    </div>
    <div class="list-item">
      <div class="item-head"><svg viewBox="0 0 14 14"><circle cx="7" cy="7" r="6" fill="none" stroke="#f26b21" stroke-width="1.4"/><path d="M5.5 4 L8.5 7 L5.5 10" fill="none" stroke="#f26b21" stroke-width="1.6"/></svg>Innovation &amp; Technology</div>
      <div class="item-body">Customers can rely on us to apply the latest proven technologies on their projects, and to be on the ground floor of industry standards for new and emerging markets.</div>
    </div>
    <div class="list-item">
      <div class="item-head"><svg viewBox="0 0 14 14"><circle cx="7" cy="7" r="6" fill="none" stroke="#f26b21" stroke-width="1.4"/><path d="M5.5 4 L8.5 7 L5.5 10" fill="none" stroke="#f26b21" stroke-width="1.6"/></svg>Knowledgeable &amp; Valued Employees</div>
      <div class="item-body">Lumen recognizes that its greatest asset is its people. We pledge to treat each employee with integrity, dealing honestly with all.</div>
    </div>
  </div>

  <div class="abs brand">
    <div class="brand-dot"></div>
    <div class="brand-name">LUMEN<br>ELECTRICAL</div>
  </div>

  <div class="abs office-label">OUR OFFICE</div>
  <div class="abs map" role="img" aria-label="Street map showing the office location beside the river in East Perth"></div>

  <div class="abs contact">
    <div class="contact-row contact-row--phone">
      <svg viewBox="0 0 14 14"><path d="M3 1.5 L5 1.5 L6 4.5 L4.6 5.6 C5.4 7.3 6.7 8.6 8.4 9.4 L9.5 8 L12.5 9 L12.5 11 C12.5 12 11.8 12.5 11 12.5 C5.8 12.2 1.8 8.2 1.5 3 C1.5 2.2 2 1.5 3 1.5 Z" fill="#f26b21"/></svg>
      1300 555 014
    </div>
    <div class="contact-row">
      <svg viewBox="0 0 14 14"><path d="M7 1.5 L13 7 L11 7 L11 12.5 L8.5 12.5 L8.5 9 L5.5 9 L5.5 12.5 L3 12.5 L3 7 L1 7 Z" fill="#f26b21"/></svg>
      <span>24 Corbel Lane, East<br>Perth WA 6004</span>
    </div>
    <div class="contact-row">
      <svg viewBox="0 0 14 14"><rect x="1.5" y="3" width="11" height="8" fill="#f26b21"/><path d="M1.5 3 L7 7.5 L12.5 3" fill="none" stroke="#fff" stroke-width="1.2"/></svg>
      info@lumenelec.com.au
    </div>
    <div class="contact-row">
      <svg viewBox="0 0 14 14"><circle cx="7" cy="7" r="5.5" fill="none" stroke="#f26b21" stroke-width="1.2"/><ellipse cx="7" cy="7" rx="2.4" ry="5.5" fill="none" stroke="#f26b21" stroke-width="1"/><path d="M1.5 7 H12.5" stroke="#f26b21" stroke-width="1"/></svg>
      www.lumenelec.com.au
    </div>
  </div>

  <div class="abs foot-bar"></div>
</div>
</body>
</html>
```